Webdesign für Vermietung eines Ferienhauses auf der Insel Usedom
Zielgruppe
Vermietung eines Ferienhauses auf der Insel Usedom
ZG: Urlauber im gehobenem Preissegment, die Luxus schätzen und urlauben wollen
Aufgabenstellung
- IN ADOBE PHOTOSHOP
- Bilder können hier entnommen werden: https://www.quartiro-net.example/ob-link-ansicht-reserve/index.php?portal=48127&unit=39502/index.html
- gern können Sie auch Stock-Bilder verwenden
- Der Buchungskalender /die Verfügbarkeit der freien Zeiträume soll präsent im oberen Bereich der Seite stehen
- Lumivo-Bewertungsbutton
- Es gibt kein Logo - bitte den Namenszug 'KIEFERNVILLA*****HOLMSTEDE' nutzen

```html
<!DOCTYPE html>
<html lang="de">
<head>
<meta charset="utf-8">
<title>Kiefernvilla Holmstede – Ferienhaus</title>
<link href="https://fonts.googleapis.com/css2?family=Montserrat:wght@400;500;600;700;800&display=swap" rel="stylesheet">
<style>
:root{
  --gold:#bd8705;
  --gold-dark:#b07d00;
  --text:#333333;
  --muted:#8a8a8a;
  --green:#7fa072;
  --rust:#b5552c;
  --band:#f3f3ef;
  --panel:#f4f4f2;
  --footer:#393939;
  --white:#ffffff;
}
*{box-sizing:border-box;margin:0;padding:0}
html,body{width:1200px;height:2867px;overflow:hidden}
body{position:relative;background:var(--white);font-family:"Montserrat",sans-serif;color:var(--text)}
.abs{position:absolute}

/* header */
.site-header{position:absolute;left:0;top:0;width:1200px;height:75px;background:var(--white)}
.brand{position:absolute;left:83px;top:17px;text-align:center;color:var(--gold);font-weight:800;font-size:15.5px;line-height:15px;letter-spacing:0.2px}
.brand .stars{font-size:9px;line-height:9px;letter-spacing:2px}
.main-nav{position:absolute;top:29px;left:0;font-size:14.5px;color:var(--muted);font-weight:500}
.main-nav a{position:absolute;white-space:nowrap;color:inherit;text-decoration:none}
.main-nav a.active{color:var(--gold);font-weight:600}

/* hero */
.hero{position:absolute;left:0;top:75px;width:1200px;height:584px;
  background:linear-gradient(180deg,rgba(0,0,0,0) 80%,rgba(40,40,40,.55) 100%),
  linear-gradient(100deg,#4d5e3a 0%,#7d8a6a 18%,#8b7a62 30%,#c9c6bd 45%,#e6e4de 60%,#b8b3a6 78%,#4f5c3b 100%)}
.hero-arrow{position:absolute;top:340px;width:26px;height:50px}
.hero-card{position:absolute;left:83px;top:336px;width:441px;height:267px;background:rgba(242,242,240,.88);padding:0 30px}
.hero-card h1{position:absolute;left:32px;top:20px;font-weight:500;color:var(--gold);font-size:52px;line-height:47px}
.hero-card p{position:absolute;left:36px;top:123px;width:380px;font-size:16px;line-height:23.5px;font-weight:500;color:#3a3a3a}
.btn-outline{position:absolute;left:31px;top:208px;width:212px;height:34px;border:2px solid var(--gold);border-radius:17px;color:var(--gold);font-weight:700;font-size:14px;line-height:30px;text-align:center}

/* intro */
.intro-title{left:85px;top:722px;font-size:28px;font-weight:600;color:var(--gold)}
.intro-text{left:85px;top:766px;width:335px;font-size:15.3px;line-height:20px;font-weight:500}
.rating{left:75px;top:982px;width:190px;height:109px;background:var(--panel);padding:10px 0 0 25px}
.rating .name{font-size:21px;font-weight:600;color:var(--gold);line-height:24px}
.rating .stars{display:flex;gap:7px;margin-top:2px}
.rating .label{font-size:14.5px;line-height:19px;font-weight:500;margin-top:3px}

/* calendar */
.calendar{left:499px;top:711px;width:613px;height:380px;background:var(--panel);border:2px solid var(--gold);box-shadow:0 4px 14px rgba(0,0,0,.22)}
.cal-head{position:absolute;left:0;top:0;width:609px;height:41px;border-bottom:1px solid #d6c8a0}
.cal-month{position:absolute;top:12px;font-size:14.5px;font-weight:600}
.cal-nav{position:absolute;top:7px;width:27px;height:27px}
.weekdays,.days{position:absolute;display:grid;grid-template-columns:repeat(7,31px);column-gap:5.75px}
.weekdays{top:62px;font-size:12.5px;color:var(--muted);text-align:center}
.days{top:76px;grid-auto-rows:21px;row-gap:5px}
.day{font-size:12px;font-weight:600;color:var(--white);text-align:center;line-height:21px}
.free{background:var(--green)}
.taken{background:var(--rust)}
.picked{background:var(--gold-dark);color:#3a2a00}
.split{background:linear-gradient(135deg,var(--green) 50%,var(--rust) 50%)}
.legend{position:absolute;top:255px;left:68px;display:flex;gap:14px;font-size:10px;color:var(--muted)}
.legend span{display:flex;align-items:center;gap:6px}
.legend i{display:inline-block;width:17px;height:11px}
.split-in{background:linear-gradient(135deg,var(--rust) 50%,var(--green) 50%)}
.btn-check{position:absolute;left:26px;top:303px;width:559px;height:46px;border-radius:23px;background:var(--gold);color:var(--white);font-weight:600;font-size:14.5px;line-height:46px;text-align:center}

/* facts */
.facts{left:0;top:1154px;width:1200px;height:182px;background:var(--band)}
.fact{position:absolute;font-size:15px;line-height:21.5px;font-weight:500}

/* gallery */
.gallery-photo{left:289px;top:1408px;width:599px;height:398px;background:linear-gradient(100deg,#d9d9d6 0%,#f1f0ec 30%,#cfc6b6 50%,#e9e7e1 70%,#5c5a56 95%)}
.gallery-arrow{position:absolute;top:160px;width:24px;height:56px}
.caption{position:absolute;left:6px;top:362px;width:239px;height:30px;background:rgba(255,255,255,.85);font-size:8.2px;font-weight:600;line-height:11px;padding:4px 0 0 7px}
.thumbs{left:327px;top:1822px;display:flex;gap:10px}
.thumb{width:79px;height:49px}
.circle-btn{position:absolute;width:27px;height:27px}

/* map */
.map{left:0;top:1958px;width:1200px;height:344px;background:linear-gradient(115deg,#ede5cf 0%,#ede5cf 55%,#a9c6ee 62%,#a9c6ee 100%)}

/* info */
.info-title{left:82px;top:2343px;font-size:28px;font-weight:600;color:var(--gold)}
.info-col{top:2393px;width:498px;font-size:15.2px;line-height:20px}
.info-col p+p{margin-top:20px}

/* footer */
.site-footer{left:0;top:2686px;width:1200px;height:181px;background:var(--footer);text-align:center}
.site-footer .brand{position:absolute;left:0;top:34px;width:1200px;font-size:21px;line-height:20px}
.site-footer .brand .stars{font-size:12px;line-height:13px}
.footer-address{position:absolute;left:0;top:100px;width:1200px;color:var(--white);font-size:15px;font-weight:500}
.footer-legal{position:absolute;left:0;top:153px;width:1200px;color:#d8d8d8;font-size:8.5px;font-weight:500}
</style>
</head>
<body>

<header class="site-header">
  <div class="brand">KIEFERNVILLA<div class="stars">★★★★★</div>HOLMSTEDE</div>
  <nav class="main-nav">
    <a class="active" style="left:294px">Start</a>
    <a style="left:396px">Das 5* Strandhaus</a>
    <a style="left:591px">Verfügbarkeit</a>
    <a style="left:755px">Die Räumlichkeiten</a>
    <a style="left:961px">Lage</a>
    <a style="left:1059px">Kontakt</a>
  </nav>
</header>

<section class="hero" role="img" aria-label="Foto: reetgedecktes Strandhaus mit Holzfassade zwischen Kiefern">
  <svg class="hero-arrow" style="left:22px" viewBox="0 0 26 50"><path d="M22 3 L4 25 L22 47" fill="none" stroke="#fff" stroke-width="3"/></svg>
  <svg class="hero-arrow" style="left:1130px" viewBox="0 0 26 50"><path d="M4 3 L22 25 L4 47" fill="none" stroke="#fff" stroke-width="3"/></svg>
</section>
<div class="hero-card" style="position:absolute">
  <h1>Welcome<br>Home</h1>
  <p>5-Sterne-Ferienhaus mit großzügigen, schilfrohrgedeckten Strandhaus in Holmstede auf der wunderschönen Insel Usedom.</p>
  <div class="btn-outline">Das 5* Strandhaus</div>
</div>

<h2 class="abs intro-title">Reif für die Insel?</h2>
<p class="abs intro-text">"NORVAL Küstenland" in Holmstede ist eine in Mecklenburg-Vorpommern einzigartige 5-Sterne-Ferienhaus-Anlage mit 42 groß­zügigen, schilfrohrgedeckten Strandhäusern mit bis zu 225 m² Wohnfläche und 26 Ferienwohnungen. Dieses exklusive, 2017 erbaute Strandhaus mit ca. 145 m² Wohnfläche und einem Grundstück von ca. 700 m² befindet sich ca. 5 Gehminuten vom Strand entfernt.</p>

<div class="abs rating">
  <div class="name">Lumivo</div>
  <div class="stars">
    <svg width="17" height="16" viewBox="0 0 24 23"><path d="M12 1l3.3 7 7.6.8-5.7 5.1 1.7 7.5L12 17.5 5.1 21.4l1.7-7.5L1.1 8.8 8.7 8z" fill="#f0a81e"/></svg>
    <svg width="17" height="16" viewBox="0 0 24 23"><path d="M12 1l3.3 7 7.6.8-5.7 5.1 1.7 7.5L12 17.5 5.1 21.4l1.7-7.5L1.1 8.8 8.7 8z" fill="#f0a81e"/></svg>
    <svg width="17" height="16" viewBox="0 0 24 23"><path d="M12 1l3.3 7 7.6.8-5.7 5.1 1.7 7.5L12 17.5 5.1 21.4l1.7-7.5L1.1 8.8 8.7 8z" fill="#f0a81e"/></svg>
    <svg width="17" height="16" viewBox="0 0 24 23"><path d="M12 1l3.3 7 7.6.8-5.7 5.1 1.7 7.5L12 17.5 5.1 21.4l1.7-7.5L1.1 8.8 8.7 8z" fill="#f0a81e"/></svg>
    <svg width="17" height="16" viewBox="0 0 24 23"><path d="M12 1l3.3 7 7.6.8-5.7 5.1 1.7 7.5L12 17.5 5.1 21.4l1.7-7.5L1.1 8.8 8.7 8z" fill="#f0a81e"/></svg>
  </div>
  <div class="label">5 Sterne von 5 bei<br>25 Bewertungen</div>
</div>

<div class="abs calendar">
  <div class="cal-head">
    <svg class="cal-nav" style="left:11px" viewBox="0 0 27 27"><circle cx="13.5" cy="13.5" r="13.5" fill="var(--gold)"/><path d="M16 7 L10 13.5 L16 20" fill="none" stroke="#fff" stroke-width="3"/></svg>
    <div class="cal-month" style="left:96px">Dezember 2022</div>
    <div class="cal-month" style="left:417px">Januar 2023</div>
    <svg class="cal-nav" style="left:577px" viewBox="0 0 27 27"><circle cx="13.5" cy="13.5" r="13.5" fill="var(--gold)"/><path d="M11 7 L17 13.5 L11 20" fill="none" stroke="#fff" stroke-width="3"/></svg>
  </div>

  <div class="weekdays" style="left:26px"><span>Mo</span><span>Di</span><span>Mi</span><span>Do</span><span>Fr</span><span>Sa</span><span>So</span></div>
  <div class="days" style="left:26px">
    <span></span><span></span><span></span>
    <span class="day free">01</span><span class="day free">02</span><span class="day free">03</span><span class="day free">04</span>
    <span class="day free">05</span><span class="day free">06</span><span class="day free">07</span><span class="day free">08</span><span class="day free">09</span><span class="day free">10</span><span class="day free">11</span>
    <span class="day picked">12</span><span class="day picked">13</span><span class="day picked">14</span><span class="day picked">15</span><span class="day picked">16</span><span class="day free">17</span><span class="day free">18</span>
    <span class="day free">19</span><span class="day free">20</span><span class="day free">21</span><span class="day free">22</span><span class="day free">23</span><span class="day free">24</span><span class="day free">25</span>
    <span class="day free">26</span><span class="day free">27</span><span class="day free">28</span><span class="day free">29</span><span class="day free">30</span><span class="day split">31</span>
  </div>

  <div class="weekdays" style="left:332px"><span>Mo</span><span>Di</span><span>Mi</span><span>Do</span><span>Fr</span><span>Sa</span><span>So</span></div>
  <div class="days" style="left:332px">
    <span></span><span></span><span></span><span></span><span></span><span></span>
    <span class="day taken">01</span>
    <span class="day taken">02</span><span class="day taken">03</span><span class="day taken">04</span><span class="day taken">05</span><span class="day taken">06</span><span class="day taken">07</span><span class="day taken">08</span>
    <span class="day taken">09</span><span class="day taken">10</span><span class="day taken">11</span><span class="day taken">12</span><span class="day taken">13</span><span class="day taken">14</span><span class="day taken">15</span>
    <span class="day taken">16</span><span class="day taken">17</span><span class="day taken">18</span><span class="day taken">19</span><span class="day taken">20</span><span class="day taken">21</span><span class="day taken">22</span>
    <span class="day taken">23</span><span class="day taken">24</span><span class="day taken">25</span><span class="day taken">26</span><span class="day taken">27</span><span class="day taken">28</span><span class="day taken">29</span>
    <span class="day taken">30</span><span class="day taken">31</span>
  </div>

  <div class="legend">
    <span><i class="taken"></i>nicht verfügbar</span>
    <span><i class="free"></i>verfügbar</span>
    <span><i class="split-in"></i>möglicher Anreisetag</span>
    <span><i class="split"></i>möglicher Abreisetag</span>
  </div>
  <div class="btn-check">Verfügbarkeit prüfen</div>
</div>

<section class="abs facts">
  <svg class="abs" style="left:114px;top:59px" width="50" height="50" viewBox="0 0 50 50">
    <path d="M22 1l3.5 7.2 7.9.9-5.9 5.4 1.7 7.8L22 18.3l-7.2 4 1.7-7.8-5.9-5.4 7.9-.9z" fill="var(--gold)"/>
    <path d="M4 46V24h42v22M4 36h42M10 31v-6h12v6M28 31v-6h12v6M4 46h5M41 46h5" fill="none" stroke="#666" stroke-width="2.5"/>
  </svg>
  <div class="fact" style="left:176px;top:59px">Schlafzimmer: 3<br>Badezimmer: 2<br>Sauna &amp; Whirlpool</div>

  <svg class="abs" style="left:525px;top:64px" width="46" height="46" viewBox="0 0 46 46">
    <path d="M23 1v5M10 6l3 4M36 6l-3 4M3 15l5 2M43 15l-5 2" stroke="var(--gold)" stroke-width="2.5"/>
    <path d="M8 34a15 15 0 0 1 30 0z" fill="var(--gold)"/>
    <circle cx="23" cy="17" r="2.5" fill="#666"/>
    <path d="M3 37h40M6 43h34" stroke="#666" stroke-width="3"/>
  </svg>
  <div class="fact" style="left:590px;top:70px">Check-in: 16:00h<br>Check-out: 10:00h</div>

  <svg class="abs" style="left:890px;top:62px" width="36" height="48" viewBox="0 0 36 48">
    <path d="M18 46C10 34 2 25 2 17a16 16 0 0 1 32 0c0 8-8 17-16 29z" fill="none" stroke="#666" stroke-width="2.5"/>
    <circle cx="18" cy="17" r="9" fill="none" stroke="#666" stroke-width="2"/>
    <circle cx="18" cy="17" r="6" fill="var(--gold)"/>
  </svg>
  <div class="fact" style="left:945px;top:70px">5 min. Strand<br>1 km zum Zentrum</div>
</section>

<div class="abs gallery-photo" role="img" aria-label="Foto: Wohnbereich mit Kaminofen, Treppe und Essplatz">
  <svg class="gallery-arrow" style="left:24px" viewBox="0 0 24 56"><path d="M20 3L4 28l16 25" fill="none" stroke="#fff" stroke-width="3"/></svg>
  <svg class="gallery-arrow" style="left:552px" viewBox="0 0 24 56"><path d="M4 3l16 25-16 25" fill="none" stroke="#fff" stroke-width="3"/></svg>
  <div class="caption">Estas Wohnzimmer mit Kamin estas resta justas<br>negare tres luxus eras petras kala.</div>
</div>
<svg class="circle-btn" style="left:294px;top:1833px" viewBox="0 0 27 27"><circle cx="13.5" cy="13.5" r="13.5" fill="var(--gold)"/><path d="M16 7L10 13.5 16 20" fill="none" stroke="#fff" stroke-width="3"/></svg>
<div class="abs thumbs">
  <div class="thumb" role="img" aria-label="Foto: Haus bei Nacht" style="background:linear-gradient(180deg,#0f1e3a,#3a2a4a 60%,#b23a3a)"></div>
  <div class="thumb" role="img" aria-label="Foto: Haus im Schnee" style="background:linear-gradient(180deg,#dfe3ea,#8b93a3)"></div>
  <div class="thumb" role="img" aria-label="Foto: Terrasse mit Garten" style="background:linear-gradient(180deg,#c9cdc4,#6f7d5a)"></div>
  <div class="thumb" role="img" aria-label="Foto: Whirlpool mit Beleuchtung" style="background:linear-gradient(180deg,#0f3d48,#2aa6b3)"></div>
  <div class="thumb" role="img" aria-label="Foto: Essbereich" style="background:linear-gradient(180deg,#efece5,#a89b85)"></div>
  <div class="thumb" role="img" aria-label="Foto: Küche" style="background:linear-gradient(180deg,#d8d8d4,#54565a)"></div>
</div>
<svg class="circle-btn" style="left:859px;top:1833px" viewBox="0 0 27 27"><circle cx="13.5" cy="13.5" r="13.5" fill="var(--gold)"/><path d="M11 7l6 6.5L11 20" fill="none" stroke="#fff" stroke-width="3"/></svg>

<div class="abs map" role="img" aria-label="Karte: Lage des Hauses in Holmstede an der Ostseeküste"></div>

<h2 class="abs info-title">Allgemeine Informationen</h2>
<div class="abs info-col" style="left:82px">
  <p>Lorem ipsum dolor sit amet, consectetuer adipiscing elit. Aenean commodo ligula eget dolor. Aenean massa. Cum sociis natoque penatibus et magnis dis parturient montes, nascetur ridiculus mus. Donec quam felis, ultricies nec, pellentesque eu, pretium quis, sem. Nulla consequat massa quis enim. Donec pede justo, fringilla vel, aliquet nec, vulputate eget, arcu. In enim justo, rhoncus ut, imperdiet a, venenatis vitae, justo. Nullam dictum felis eu pede mollis pretium. Integer tincidunt. Cras dapibus. Vivamus elementum semper nisi. Aenean vulputate eleifend tellus. Aenean leo ligula, porttitor eu, consequat vitae, eleifend ac, enim. Aliquam lorem ante, dapibus in, viverra quis, feugiat a, tellus. Phasellus viverra nulla ut metus varius</p>
</div>
<div class="abs info-col" style="left:611px">
  <p>laoreet. Quisque rutrum. Aenean imperdiet. Etiam ultricies nisi vel augue. Curabitur ullamcorper ultricies nisi. Nam eget dui. Etiam rhoncus. Maecenas tempus, tellus eget condimentum rhoncus, sem quam semper libero, sit amet adipiscing sem neque sed ipsum. Nam quam nunc, blandit vel, luctus pulvinar, hendrerit id, lorem.</p>
  <p>Maecenas nec odio et ante tincidunt tempus. Donec vitae sapien ut libero venenatis faucibus. Nullam quis ante. Etiam sit amet orci eget eros faucibus tincidunt. Duis leo. Sed fringilla mauris sit amet nibh. Donec sodales sagittis magna Sede est.</p>
</div>

<footer class="abs site-footer">
  <div class="brand">KIEFERNVILLA<div class="stars">★★★★★</div>HOLMSTEDE</div>
  <div class="footer-address">Holmstede - Dünenweg 12b</div>
  <div class="footer-legal">© 2022 Kiefernvilla Holmstede | Impressum | Datenschutz</div>
</footer>

</body>
</html>
```